Template for Tolvik Advisory PowerPoint

We would like to create a new template for PowerPoint based on our current logo and graphic design guidelines. The template should reflect our corporate identity and be easy to use to create different kind of PowerPoint presentations for different kind of customers. The current design guideline that are attached reflect the "old" look of the PPT design and is only to be seen as a reference.
Tolvik Advisory is a Management consulting company working within both public and private sector. We focus on strategic business development and work in close cooperation with the customer to make sure it is the customer that will become the hero, our work is to support and guide them to the top.
The design should reflect a modern company working in close cooperation with our customers to help them innovate and describe their future business model, and also help them to reach that goal!
Words and taglines that we use. Passion for the future. The power of the organisation. Power of thoughts. Inspiration. Engagement.
What we have in mind is a modern, clean and elegant design based on our current logo. Tolvik Advisory is a Swedish Company working primarily on the Swedish market so the template must be possible to translate to Swedish (however the design can be done in english and be translated later)

Reason: I would like to extend the deadline to receive some more alternatives!

Reason: I'm out travelling and would like to extend the timeline to be able to choose the right design for our template. /Henrik

Target Market(s)

Our target market is within both private and public sector. Our main focus is CxO level executives within our clients organisation.

Industry/Entity Type

Management Consulting

Font styles to use
Sans Serif

Colors

Designer to choose colors to be used in the design.

Requirements
Must have
• A PPT template that contains both slides for traditional text and graphic. We like to work a lot with graphical presentations and try to limit the text on our slides to a minimum.
Nice to have
• Slides for different chapters within the presentation. Slides for powerful one-liners. Title slides. Thank you slides at the end.
Should not have
• Massive text....

```html
<!DOCTYPE html>
<html lang="en">
<head>
<meta charset="utf-8">
<title>Tolvik Advisory – Presentation Template Overview</title>
<link href="https://fonts.googleapis.com/css2?family=Didact+Gothic&family=Montserrat:wght@600;700&display=swap" rel="stylesheet">
<style>
:root{
  --red:#c0223f; --red-dark:#a81c36; --blue:#135b8e; --olive:#8c8a5c; --grey:#9aa1a6;
  --lav:#c9c2e3; --band:#b3b6bf; --ink:#4a4a4a; --white:#fff;
}
*{margin:0;padding:0;box-sizing:border-box}
html,body{width:1200px;height:1200px;overflow:hidden}
body{background:var(--lav);position:relative;font-family:"Didact Gothic",sans-serif;color:var(--ink)}
.band{position:absolute;background:var(--band)}
.slide{position:absolute;width:172px;height:128px;background:var(--white);overflow:hidden;box-shadow:0 1px 3px rgba(0,0,0,.35)}
.num{position:absolute;font:700 9px "Montserrat",sans-serif;color:#555}
.ab{position:absolute}
.ttl{position:absolute;left:9px;top:8px;font-size:7px;color:var(--red)}
.ttl::after{content:"";display:block;width:14px;height:1px;background:var(--red);margin-top:2px}
.logo{position:absolute;right:7px;top:7px;font-size:4px;color:var(--red);display:flex;align-items:center;gap:1px}
.logo i{width:3px;height:3px;border-radius:50%;background:currentColor;display:inline-block}
.foot{position:absolute;left:4px;right:4px;bottom:3px;height:6px}
.foot::before{content:"";position:absolute;left:0;right:14px;bottom:3px;height:1.5px;background:var(--blue)}
.foot::after{content:"";position:absolute;right:0;width:14px;bottom:3px;height:1.5px;background:var(--red)}
.foot span{position:absolute;bottom:0;font-size:2.4px;color:var(--blue)}
.foot span+span{right:2px;color:var(--red)}
.tx{position:absolute;font-size:3px;line-height:1.35;color:#555}
.tx.w{color:#fff}
.photo{position:absolute}
.p-mtn{background:linear-gradient(180deg,#4d6a9a 0%,#8b9bb8 40%,#e8ecf2 60%,#6f6a62 100%)}
.p-team{background:linear-gradient(135deg,#5b4a3c,#b8a48a 50%,#2d3038)}
.p-wb{background:linear-gradient(120deg,#f2f2f2,#d6d6d6 55%,#8a6e5a)}
.p-ski{background:linear-gradient(180deg,#d8e2ee,#b8c6d8 55%,#c0223f 56%,#c0223f 100%)}
.p-city{background:linear-gradient(90deg,#6d7f98,#c6d0dc 60%,#3f4f66)}
.p-lake{background:linear-gradient(180deg,#c9d6e0,#7d8f92 50%,#3e5560)}
.p-man{background:linear-gradient(180deg,#8a6c58,#3b3432)}
.red{background:var(--red)} .blue{background:var(--blue)} .olive{background:var(--olive)} .greyb{background:var(--grey)}
.chip{position:absolute;height:5px;padding:0 3px;font-size:2.6px;line-height:5px;color:#fff;background:var(--red);border-radius:1px}
.dot{position:absolute;border-radius:50%}
.big{position:absolute;color:var(--red);text-align:center;width:100%}
.inv{color:#fff}
</style>
</head>
<body>
<div class="band" style="left:0;top:0;width:1026px;height:464px"></div>
<div class="band" style="left:0;top:466px;width:1034px;height:450px"></div>
<div class="band" style="left:16px;top:918px;width:822px;height:158px"></div>

<!-- Row 1 -->
<div class="slide" style="left:8px;top:2px">
  <div class="photo p-mtn" style="left:0;top:0;width:172px;height:52px" role="img" aria-label="Mountain landscape with prayer flags"></div>
  <div class="ab red" style="left:12px;top:0;width:22px;height:24px"></div>
  <div class="ab inv" style="left:15px;top:16px;font-size:4px">tolvik</div>
  <div class="big" style="top:72px;font-size:7px">PRESENTATIONTITLE</div>
  <div class="tx" style="left:20px;top:86px;width:132px;text-align:center">We focus on strategic business development and work in close cooperation with the customer to make sure it is the customer that will become the hero, our work is to support and guide them to the top.</div>
</div>
<div class="num" style="left:170px;top:138px">1</div>

<div class="slide" style="left:218px;top:2px">
  <div class="ab red" style="left:8px;top:0;width:26px;height:30px"></div>
  <div class="ab inv" style="left:10px;top:22px;font-size:4px">tolvik</div>
  <div class="ab" style="left:48px;top:16px;font-size:7px;color:var(--red)">PRESENTATIONTITLE</div>
  <div class="ab" style="left:34px;top:30px;width:138px;height:1px;background:var(--red)"></div>
  <div class="photo p-mtn" style="left:0;top:31px;width:172px;height:55px" role="img" aria-label="Mountain landscape with prayer flags"></div>
  <div class="tx" style="left:24px;top:96px;width:124px;text-align:center">Tolvik Advisory Is A Management Consulting Company Working Within Both Public And Private Sector.</div>
</div>
<div class="num" style="left:380px;top:138px">2</div>

<div class="slide" style="left:427px;top:2px">
  <div class="ab" style="left:32px;top:18px;font-size:6px;color:var(--red)">AGENDA</div>
  <div class="ab" style="left:32px;top:26px;width:14px;height:1px;background:var(--red)"></div>
  <div class="tx" style="left:32px;top:36px;font-size:4px;line-height:2.6"><span style="color:var(--red)">01.</span> Mission<br><span style="color:var(--red)">02.</span> Today's Situation<br><span style="color:var(--red)">03.</span> Why Invest?</div>
  <div class="photo p-mtn" style="left:110px;top:0;width:62px;height:128px" role="img" aria-label="Mountain peak with prayer flags"></div>
</div>
<div class="num" style="left:590px;top:138px">3</div>

<div class="slide" style="left:637px;top:2px">
  <div class="ttl">Sample Text</div><div class="logo">tolvik<i></i></div>
  <div class="photo p-team" style="left:54px;top:24px;width:66px;height:34px" role="img" aria-label="Business team meeting"></div>
  <div class="dot blue" style="left:36px;top:68px;width:8px;height:8px"></div>
  <div class="dot blue" style="left:82px;top:68px;width:8px;height:8px"></div>
  <div class="dot blue" style="left:128px;top:68px;width:8px;height:8px"></div>
  <div class="chip" style="left:30px;top:80px">Sample Text</div>
  <div class="chip" style="left:76px;top:80px">Sample Text</div>
  <div class="chip" style="left:122px;top:80px">Sample Text</div>
  <div class="tx" style="left:14px;top:90px;width:40px">We focus on strategic business development so the customer becomes the hero and reaches the top.</div>
  <div class="tx" style="left:66px;top:90px;width:40px">We focus on strategic business development so the customer becomes the hero and reaches the top.</div>
  <div class="tx" style="left:118px;top:90px;width:40px">We focus on strategic business development so the customer becomes the hero and reaches the top.</div>
  <div class="foot"><span>www.tolvik-advisory.se</span><span>Page • 4</span></div>
</div>
<div class="num" style="left:800px;top:138px">4</div>

<div class="slide" style="left:846px;top:2px">
  <div class="ttl">Sample Text</div><div class="logo">tolvik<i></i></div>
  <div class="photo p-team" style="left:0;top:22px;width:100px;height:56px" role="img" aria-label="Smiling businesswoman in meeting"></div>
  <div class="ab" style="left:100px;top:24px;width:72px;height:54px;background:#c95058"></div>
  <div class="dot" style="left:140px;top:28px;width:8px;height:8px;border:1px solid #fff"></div>
  <div class="tx w" style="left:112px;top:40px;width:52px">We focus on strategic business development and work in close cooperation with the customer so they become the hero.</div>
  <div class="tx" style="left:10px;top:84px;width:82px">We focus on strategic business development and work in close cooperation with the customer to make sure it is the customer that will become the hero.</div>
  <div class="foot"><span>www.tolvik-advisory.se</span><span>Page • 4</span></div>
</div>
<div class="num" style="left:1008px;top:138px">5</div>

<div class="slide" style="left:1028px;top:4px">
  <div class="logo">tolvik<i></i></div>
  <div class="dot blue" style="left:80px;top:28px;width:11px;height:11px"></div>
  <div class="ab" style="left:83px;top:29px;font:700 7px Montserrat,sans-serif;color:#fff">“</div>
  <div class="ab" style="left:10px;top:48px;width:152px;text-align:center;font:700 4.4px/1.6 Montserrat,sans-serif;color:var(--red)">We Are A Boutique Executive Search Company (Aka Headhunter) For Professionals And Executives With A Strong Digital Background.</div>
  <div class="foot"><span>www.tolvik-advisory.se</span><span>Page • 6</span></div>
</div>

<!-- Row 2 -->
<div class="slide" style="left:8px;top:160px">
  <div class="photo p-ski" style="left:26px;top:0;width:50px;height:120px" role="img" aria-label="Skier beside a winter sports banner"></div>
  <div class="ttl" style="left:80px;top:18px">Sample Text</div>
  <div class="ab" style="left:76px;top:32px;width:96px;height:36px;background:#c95058"></div>
  <div class="dot" style="left:80px;top:38px;width:8px;height:8px;border:1px solid #fff"></div>
  <div class="tx w" style="left:92px;top:38px;width:74px">We focus on strategic business development and work in close cooperation with the customer to make sure it is the customer that becomes the hero.</div>
  <div class="dot" style="left:80px;top:78px;width:8px;height:8px;border:1px solid #ccc"></div>
  <div class="tx" style="left:92px;top:78px;width:74px">We focus on strategic business development and work in close cooperation with the customer to make sure it is the customer that becomes the hero.</div>
  <div class="foot"><span>www.tolvik-advisory.se</span><span>Page • 4</span></div>
</div>
<div class="num" style="left:170px;top:296px">6</div>

<div class="slide" style="left:218px;top:160px">
  <div class="ttl">Sample Text</div><div class="logo">tolvik<i></i></div>
  <div class="ab blue" style="left:6px;top:28px;width:58px;height:30px"></div>
  <div class="tx w" style="left:12px;top:32px;width:46px">We focus on strategic business development so the customer becomes the hero.</div>
  <div class="photo p-ski" style="left:64px;top:22px;width:44px;height:96px" role="img" aria-label="Skier beside a winter sports banner"></div>
  <div class="ab red" style="left:108px;top:28px;width:58px;height:30px"></div>
  <div class="tx w" style="left:114px;top:32px;width:46px">We focus on strategic business development so the customer becomes the hero.</div>
  <div class="tx" style="left:12px;top:64px;width:48px">We focus on strategic business development and work in close cooperation with the customer to make sure it is the customer that will become the hero.</div>
  <div class="tx" style="left:114px;top:64px;width:48px">We focus on strategic business development and work in close cooperation with the customer to make sure it is the customer that will become the hero.</div>
  <div class="foot"><span>www.tolvik-advisory.se</span><span>Page • 4</span></div>
</div>
<div class="num" style="left:380px;top:296px">7</div>

<div class="slide" style="left:427px;top:160px">
  <div class="ttl">Sample Text</div>
  <div class="ab blue" style="left:0;top:26px;width:120px;height:26px"></div>
  <div class="tx w" style="left:10px;top:30px;width:104px">We focus on strategic business development and work in close cooperation with the customer to make sure it is the customer that will become the hero.</div>
  <div class="photo p-ski" style="left:120px;top:0;width:52px;height:120px" role="img" aria-label="Skier beside a winter sports banner"></div>
  <div class="dot" style="left:12px;top:62px;width:6px;height:6px;border:1px solid #bbb"></div>
  <div class="tx" style="left:24px;top:62px;width:90px">We focus on strategic business development, our work is to support and guide them to the top. We focus on strategic business for the hero.</div>
  <div class="dot" style="left:12px;top:90px;width:6px;height:6px;border:1px solid #bbb"></div>
  <div class="tx" style="left:24px;top:90px;width:90px">We focus on strategic business development, our work is to support and guide them to the top. We focus on strategic business for the hero.</div>
  <div class="foot"><span>www.tolvik-advisory.se</span><span>Page • 4</span></div>
</div>
<div class="num" style="left:590px;top:296px">8</div>

<div class="slide" style="left:637px;top:160px">
  <div class="ttl">Sample Text</div><div class="logo">tolvik<i></i></div>
  <svg class="ab" style="left:62px;top:30px" width="50" height="54" viewBox="0 0 50 54">
    <polygon points="25,2 48,14 25,26 2,14" fill="#8c8a5c"/>
    <polygon points="2,14 25,26 25,52 2,40" fill="#135b8e"/>
    <polygon points="48,14 25,26 25,52 48,40" fill="#c0223f"/>
    <polygon points="2,14 25,2 25,26" fill="#9aa1a6"/>
  </svg>
  <div class="tx" style="left:10px;top:30px;width:46px"><span style="color:var(--red)">Sample Text</span><br>We focus on strategic business development and work so the customer becomes the hero.</div>
  <div class="tx" style="left:118px;top:36px;width:46px"><span style="color:var(--olive)">Sample Text</span><br>We focus on strategic business development and work so the customer becomes the hero.</div>
  <div class="tx" style="left:84px;top:86px;width:58px"><span style="color:var(--red)">Sample Text</span><br>We focus on strategic business development and work so the customer becomes the hero.</div>
  <div class="foot"><span>www.tolvik-advisory.se</span><span>Page • 4</span></div>
</div>
<div class="num" style="left:800px;top:296px">9</div>

<div class="slide" style="left:846px;top:160px">
  <div class="ttl">Sample Text</div><div class="logo">tolvik<i></i></div>
  <svg class="ab" style="left:10px;top:40px" width="64" height="40" viewBox="0 0 64 40">
    <rect x="6" y="14" width="12" height="12" transform="rotate(45 12 20)" fill="#fff" stroke="#c0223f"/>
    <rect x="26" y="2" width="12" height="12" transform="rotate(45 32 8)" fill="#9aa1a6"/>
    <rect x="26" y="14" width="12" height="12" transform="rotate(45 32 20)" fill="#c0223f"/>
    <rect x="26" y="26" width="12" height="12" transform="rotate(45 32 32)" fill="#135b8e"/>
    <rect x="40" y="14" width="12" height="12" transform="rotate(45 46 20)" fill="#8c8a5c"/>
  </svg>
  <div class="tx" style="left:78px;top:26px;width:84px"><span style="color:var(--red)">Sample Text</span><br>We focus on strategic business development and work in close cooperation with the customer.</div>
  <div class="tx" style="left:78px;top:56px;width:84px"><span style="color:var(--olive)">Sample Text</span><br>We focus on strategic business development and work in close cooperation with the customer.</div>
  <div class="tx" style="left:78px;top:84px;width:84px"><span style="color:var(--blue)">Sample Text</span><br>We focus on strategic business development and work in close cooperation with the customer.</div>
  <div class="foot"><span>www.tolvik-advisory.se</span><span>Page • 4</span></div>
</div>
<div class="num" style="left:1008px;top:296px">10</div>

<div class="slide" style="left:1028px;top:162px">
  <div class="ttl">Sample Text</div><div class="logo">tolvik<i></i></div>
  <svg class="ab" style="left:58px;top:24px" width="56" height="72" viewBox="0 0 56 72">
    <g stroke="#135b8e" stroke-width=".8"><line x1="28" y1="36" x2="28" y2="8"/><line x1="28" y1="36" x2="6" y2="24"/><line x1="28" y1="36" x2="50" y2="24"/><line x1="28" y1="36" x2="8" y2="56"/><line x1="28" y1="36" x2="48" y2="56"/><line x1="28" y1="36" x2="28" y2="66"/></g>
    <circle cx="28" cy="36" r="10" fill="#fff" stroke="#c0223f" stroke-width="2"/><circle cx="28" cy="36" r="5" fill="#c0223f"/>
    <g fill="#fff" stroke="#135b8e"><circle cx="28" cy="8" r="4"/><circle cx="6" cy="24" r="4"/><circle cx="50" cy="24" r="4"/><circle cx="8" cy="56" r="4"/><circle cx="48" cy="56" r="4"/><circle cx="28" cy="66" r="4"/></g>
  </svg>
  <div class="chip" style="left:36px;top:30px">Sample Text</div><div class="chip" style="left:118px;top:22px">Sample Text</div>
  <div class="tx" style="left:8px;top:38px;width:48px">We focus on strategic business development so the customer becomes the hero.</div>
  <div class="tx" style="left:118px;top:30px;width:48px">We focus on strategic business development so the customer becomes the hero.</div>
  <div class="tx" style="left:8px;top:76px;width:48px">We focus on strategic business development so the customer becomes the hero.</div>
  <div class="tx" style="left:118px;top:82px;width:48px">We focus on strategic business development so the customer becomes the hero.</div>
  <div class="foot"><span>www.tolvik-advisory.se</span><span>Page • 4</span></div>
</div>

<!-- Row 3 -->
<div class="slide" style="left:8px;top:318px">
  <div class="ttl">Sample Text</div><div class="logo">tolvik<i></i></div>
  <svg class="ab" style="left:14px;top:30px" width="60" height="76" viewBox="0 0 60 76">
    <polygon points="0,2 48,2 56,12 48,22 8,22 12,12" fill="#9aa1a6"/>
    <polygon points="0,28 48,28 56,38 48,48 8,48 12,38" fill="#8c8a5c"/>
    <polygon points="0,54 48,54 56,64 48,74 8,74 12,64" fill="#135b8e"/>
  </svg>
  <div class="tx" style="left:76px;top:32px;width:84px">We focus on strategic business development and work in close cooperation with the customer for the hero.</div>
  <div class="tx" style="left:76px;top:58px;width:84px">We focus on strategic business development and work in close cooperation with the customer for the hero.</div>
  <div class="tx" style="left:76px;top:84px;width:84px">We focus on strategic business development and work in close cooperation with the customer for the hero.</div>
  <div class="foot"><span>www.tolvik-advisory.se</span><span>Page • 4</span></div>
</div>
<div class="num" style="left:170px;top:454px">11</div>

<div class="slide" style="left:218px;top:318px">
  <div class="ttl">Sample Text</div><div class="logo">tolvik<i></i></div>
  <div class="tx" style="left:10px;top:28px;width:100px"><span style="color:var(--red)">Sample Text</span><br>We focus on strategic business development and work in close cooperation with the customer so they become the hero.</div>
  <div class="tx" style="left:10px;top:50px;width:100px"><span style="color:var(--red)">Sample Text</span><br>We focus on strategic business development and work in close cooperation with the customer so they become the hero.</div>
  <div class="tx" style="left:10px;top:72px;width:100px"><span style="color:var(--red)">Sample Text</span><br>We focus on strategic business development and work in close cooperation with the customer so they become the hero.</div>
  <div class="tx" style="left:10px;top:94px;width:100px"><span style="color:var(--red)">Sample Text</span><br>We focus on strategic business development and work in close cooperation with the customer so they become the hero.</div>
  <svg class="ab" style="left:118px;top:32px" width="48" height="70" viewBox="0 0 48 70">
    <g stroke="#135b8e" stroke-width="3"><line x1="24" y1="35" x2="24" y2="8"/><line x1="24" y1="35" x2="6" y2="25"/><line x1="24" y1="35" x2="6" y2="48"/><line x1="24" y1="35" x2="24" y2="62"/></g>
    <circle cx="24" cy="35" r="11" fill="#c0223f"/><circle cx="24" cy="35" r="4" fill="#fff"/>
    <circle cx="24" cy="8" r="6" fill="#c0223f"/><circle cx="6" cy="25" r="5" fill="#135b8e"/><circle cx="6" cy="48" r="5" fill="#c0223f"/><circle cx="24" cy="62" r="6" fill="#135b8e"/>
  </svg>
  <div class="foot"><span>www.tolvik-advisory.se</span><span>Page • 4</span></div>
</div>
<div class="num" style="left:380px;top:454px">12</div>

<div class="slide" style="left:427px;top:318px">
  <div class="ttl">Sample Text</div><div class="logo">tolvik<i></i></div>
  <svg class="ab" style="left:12px;top:36px" width="50" height="60" viewBox="0 0 50 60" fill="none" stroke="#555" stroke-width="1">
    <path d="M17 38 C8 30 10 12 25 12 C40 12 42 30 33 38 L33 46 L17 46 Z"/>
    <line x1="18" y1="50" x2="32" y2="50"/><line x1="19" y1="54" x2="31" y2="54"/>
    <line x1="25" y1="2" x2="25" y2="7"/><line x1="5" y1="22" x2="1" y2="22"/><line x1="45" y1="22" x2="49" y2="22"/><line x1="9" y1="8" x2="6" y2="5"/><line x1="41" y1="8" x2="44" y2="5"/>
  </svg>
  <div class="dot" style="left:72px;top:28px;width:7px;height:7px;border:1px solid #999"></div>
  <div class="dot" style="left:72px;top:50px;width:7px;height:7px;border:1px solid #999"></div>
  <div class="dot" style="left:72px;top:72px;width:7px;height:7px;border:1px solid #999"></div>
  <div class="dot" style="left:72px;top:94px;width:7px;height:7px;border:1px solid #999"></div>
  <div class="chip" style="left:86px;top:24px">Sample Text</div><div class="tx" style="left:86px;top:31px;width:76px">We deliver IT services and solutions for the cloud and integration.</div>
  <div class="chip" style="left:86px;top:46px">Sample Text</div><div class="tx" style="left:86px;top:53px;width:76px">We deliver IT services and solutions for the cloud and integration.</div>
  <div class="chip" style="left:86px;top:68px">Sample Text</div><div class="tx" style="left:86px;top:75px;width:76px">We deliver IT services and solutions for the cloud and integration.</div>
  <div class="chip" style="left:86px;top:90px">Sample Text</div><div class="tx" style="left:86px;top:97px;width:76px">We deliver IT services and solutions for the cloud and integration.</div>
  <div class="foot"><span>www.tolvik-advisory.se</span><span>Page • 4</span></div>
</div>
<div class="num" style="left:590px;top:454px">13</div>

<div class="slide" style="left:637px;top:318px">
  <div class="ttl">Sample Text</div><div class="logo">tolvik<i></i></div>
  <svg class="ab" style="left:60px;top:38px" width="52" height="52" viewBox="0 0 52 52">
    <path d="M26 2 A24 24 0 0 1 50 26 L38 26 A12 12 0 0 0 26 14 Z" fill="#8c8a5c"/>
    <path d="M50 26 A24 24 0 0 1 26 50 L26 38 A12 12 0 0 0 38 26 Z" fill="#c0223f"/>
    <path d="M26 50 A24 24 0 0 1 2 26 L14 26 A12 12 0 0 0 26 38 Z" fill="#135b8e"/>
    <path d="M2 26 A24 24 0 0 1 26 2 L26 14 A12 12 0 0 0 14 26 Z" fill="#9aa1a6"/>
    <circle cx="26" cy="26" r="6" fill="#c0223f"/>
  </svg>
  <div class="chip" style="left:26px;top:28px">Sample Text</div><div class="chip" style="left:116px;top:28px">Sample Text</div>
  <div class="tx" style="left:10px;top:36px;width:48px">We deliver IT services and solutions for the cloud.</div>
  <div class="tx" style="left:116px;top:36px;width:48px">We deliver IT services and solutions for the cloud.</div>
  <div class="chip" style="left:26px;top:82px">Sample Text</div><div class="chip" style="left:116px;top:82px">Sample Text</div>
  <div class="tx" style="left:10px;top:90px;width:48px">We deliver IT services and solutions for the cloud.</div>
  <div class="tx" style="left:116px;top:90px;width:48px">We deliver IT services and solutions for the cloud.</div>
  <div class="foot"><span>www.tolvik-advisory.se</span><span>Page • 4</span></div>
</div>
<div class="num" style="left:800px;top:454px">14</div>

<div class="slide" style="left:846px;top:318px">
  <div class="ttl">Sample Text</div><div class="logo">tolvik<i></i></div>
  <svg class="ab" style="left:10px;top:30px" width="86" height="92" viewBox="0 0 86 92">
    <path d="M48 16 C58 4 78 4 84 10 C74 22 58 24 48 16 Z" fill="#c0223f"/>
    <path d="M30 40 C40 28 62 28 68 34 C56 46 40 48 30 40 Z" fill="#135b8e"/>
    <path d="M16 64 C26 52 48 52 54 58 C42 70 26 72 16 64 Z" fill="#c0223f"/>
    <path d="M0 88 C10 76 32 76 38 82 C26 94 10 96 0 88 Z" fill="#135b8e"/>
  </svg>
  <div class="tx" style="left:104px;top:30px;width:56px;border-right:1.5px solid var(--red);padding-right:2px">We deliver IT services and solutions for the cloud.</div>
  <div class="tx" style="left:94px;top:52px;width:56px;border-right:1.5px solid var(--blue);padding-right:2px">We deliver IT services and solutions for the cloud.</div>
  <div class="tx" style="left:84px;top:74px;width:56px;border-right:1.5px solid var(--red);padding-right:2px">We deliver IT services and solutions for the cloud.</div>
  <div class="tx" style="left:74px;top:96px;width:56px;border-right:1.5px solid var(--blue);padding-right:2px">We deliver IT services and solutions for the cloud.</div>
  <div class="foot"><span>www.tolvik-advisory.se</span><span>Page • 4</span></div>
</div>
<div class="num" style="left:1008px;top:454px">15</div>

<div class="slide" style="left:1031px;top:320px">
  <div class="logo">tolvik<i></i></div>
  <div class="ab" style="left:10px;top:36px;font-size:13px;line-height:1.3;color:var(--red)">This Is A One<br>Liner Text</div>
  <div class="foot"><span>www.tolvik-advisory.se</span><span>Page • 4</span></div>
</div>

<!-- Row 4 -->
<div class="slide" style="left:12px;top:466px">
  <div class="ttl">Sample Text</div><div class="logo">tolvik<i></i></div>
  <div class="photo p-wb" style="left:8px;top:28px;width:94px;height:86px" role="img" aria-label="Consultant sketching on a whiteboard"></div>
  <div class="ab red" style="left:90px;top:32px;width:72px;height:64px"></div>
  <div class="dot" style="left:122px;top:36px;width:6px;height:6px;border:1px solid #fff"></div>
  <div class="tx w" style="left:96px;top:44px;width:62px;text-align:center">We focus on strategic business development, our work is to guide them to the top.</div>
  <div class="dot" style="left:122px;top:64px;width:6px;height:6px;border:1px solid #fff"></div>
  <div class="tx w" style="left:96px;top:72px;width:62px;text-align:center">We focus on strategic business development, our work is to guide them to the top.</div>
  <div class="foot"><span>www.tolvik-advisory.se</span><span>Page • 4</span></div>
</div>
<div class="num" style="left:168px;top:602px">16</div>

<div class="slide" style="left:221px;top:466px">
  <div class="ttl">Sample Text</div><div class="logo">tolvik<i></i></div>
  <div class="photo p-team" style="left:8px;top:36px;width:76px;height:56px" role="img" aria-label="Business team meeting"></div>
  <div class="ab red" style="left:72px;top:28px;width:94px;height:92px"></div>
  <div class="dot" style="left:94px;top:34px;width:6px;height:6px;border:1px solid #fff"></div><div class="dot" style="left:136px;top:34px;width:6px;height:6px;border:1px solid #fff"></div>
  <div class="tx w" style="left:78px;top:42px;width:38px;text-align:center">We focus on strategic business, our work is to guide them to the top.</div>
  <div class="tx w" style="left:122px;top:42px;width:38px;text-align:center">We focus on strategic business, our work is to guide them to the top.</div>
  <div class="dot" style="left:94px;top:76px;width:6px;height:6px;border:1px solid #fff"></div><div class="dot" style="left:136px;top:76px;width:6px;height:6px;border:1px solid #fff"></div>
  <div class="tx w" style="left:78px;top:84px;width:38px;text-align:center">We focus on strategic business, our work is to guide them to the top.</div>
  <div class="tx w" style="left:122px;top:84px;width:38px;text-align:center">We focus on strategic business, our work is to guide them to the top.</div>
  <div class="foot"><span>www.tolvik-advisory.se</span><span>Page • 4</span></div>
</div>
<div class="num" style="left:378px;top:602px">17</div>

<div class="slide" style="left:431px;top:466px">
  <div class="ttl">Sample Text</div>
  <div class="tx" style="left:8px;top:34px;width:50px">We focus on strategic business development and work in close cooperation with the customer to make sure it is the customer that will become the hero, our work is to support and guide them to the top.</div>
  <div class="ab blue" style="left:70px;top:0;width:30px;height:128px"></div>
  <div class="dot" style="left:82px;top:16px;width:6px;height:6px;background:#fff"></div><div class="tx w" style="left:76px;top:24px">Sample Text</div>
  <div class="dot" style="left:82px;top:38px;width:6px;height:6px;background:#fff"></div><div class="tx w" style="left:76px;top:46px">Sample Text</div>
  <div class="dot" style="left:82px;top:60px;width:6px;height:6px;background:#fff"></div><div class="tx w" style="left:76px;top:68px">Sample Text</div>
  <div class="dot" style="left:82px;top:82px;width:6px;height:6px;background:#fff"></div><div class="tx w" style="left:76px;top:90px">Sample Text</div>
  <div class="dot" style="left:82px;top:102px;width:6px;height:6px;background:#fff"></div><div class="tx w" style="left:76px;top:110px">Sample Text</div>
  <div class="photo p-team" style="left:100px;top:0;width:72px;height:128px" role="img" aria-label="Two colleagues in discussion"></div>
</div>
<div class="num" style="left:588px;top:602px">18</div>

<div class="slide" style="left:641px;top:466px">
  <div class="ttl">Sample Text</div><div class="logo">tolvik<i></i></div>
  <svg class="ab" style="left:14px;top:30px" width="62" height="62" viewBox="0 0 62 62">
    <ellipse cx="31" cy="54" rx="30" ry="6" fill="#9aa1a6"/><rect x="1" y="42" width="60" height="12" fill="#9aa1a6"/>
    <rect x="4" y="30" width="54" height="12" fill="#c0223f"/><ellipse cx="31" cy="30" rx="27" ry="5" fill="#9aa1a6"/>
    <rect x="7" y="18" width="48" height="12" fill="#c0223f"/><ellipse cx="31" cy="18" rx="24" ry="5" fill="#9aa1a6"/>
    <rect x="10" y="6" width="42" height="12" fill="#c0223f"/><ellipse cx="31" cy="6" rx="21" ry="5" fill="#9aa1a6"/>
  </svg>
  <div class="tx" style="left:86px;top:34px;width:70px">We focus on strategic business development and work in close cooperation with the customer to make sure it is the customer that will become the hero.</div>
  <div class="foot"><span>www.tolvik-advisory.se</span><span>Page • 4</span></div>
</div>
<div class="num" style="left:798px;top:602px">19</div>

<div class="slide" style="left:850px;top:466px">
  <div class="ttl">Sample Text</div><div class="logo">tolvik<i></i></div>
  <svg class="ab" style="left:14px;top:26px" width="84" height="98" viewBox="0 0 84 98">
    <ellipse cx="42" cy="8" rx="41" ry="7" fill="#a82848"/>
    <path d="M1 8 L83 8 L66 34 L18 34 Z" fill="#c0223f"/>
    <path d="M18 36 L66 36 L56 56 L28 56 Z" fill="#b0203e"/>
    <path d="M28 58 L56 58 L50 76 L34 76 Z" fill="#8d2048"/>
    <path d="M34 78 L50 78 L44 96 L40 96 Z" fill="#6a2050"/>
  </svg>
  <div class="tx" style="left:104px;top:34px;width:56px">We focus on strategic business development and work in close cooperation with the customer to make sure it is the customer that will become the hero.</div>
  <div class="foot"><span>www.tolvik-advisory.se</span><span>Page • 4</span></div>
</div>
<div class="num" style="left:1008px;top:602px">20</div>

<div class="slide" style="left:1026px;top:464px;height:128px">
  <div class="logo">tolvik<i></i></div>
  <div class="big" style="top:42px;font-size:15px;line-height:1.35">THIS IS A ONE<br>LINER TEXT</div>
</div>

<!-- Row 5 -->
<div class="slide" style="left:12px;top:624px">
  <div class="ttl">Sample Text</div><div class="logo">tolvik<i></i></div>
  <div class="photo p-wb" style="left:30px;top:22px;width:86px;height:36px" role="img" aria-label="Consultant sketching on a whiteboard"></div>
  <div class="dot blue" style="left:122px;top:76px;width:9px;height:9px"></div>
  <div class="chip" style="left:116px;top:90px">Sample Text</div>
  <div class="tx" style="left:10px;top:78px;width:96px">We focus on strategic business development and work in close cooperation with the customer to make sure it is the customer that will become the hero.</div>
  <div class="tx" style="left:108px;top:98px;width:54px">We focus on strategic business development for the hero.</div>
  <div class="foot"><span>www.tolvik-advisory.se</span><span>Page • 4</span></div>
</div>
<div class="num" style="left:168px;top:760px">21</div>

<div class="slide" style="left:221px;top:624px">
  <div class="ttl">Sample Text</div><div class="logo">tolvik<i></i></div>
  <div class="photo p-team" style="left:22px;top:28px;width:128px;height:44px" role="img" aria-label="Business team meeting"></div>
  <div class="dot blue" style="left:30px;top:62px;width:14px;height:14px;border:1px solid #fff"></div>
  <div class="dot blue" style="left:80px;top:62px;width:14px;height:14px;border:1px solid #fff"></div>
  <div class="dot blue" style="left:130px;top:62px;width:14px;height:14px;border:1px solid #fff"></div>
  <div class="chip" style="left:26px;top:82px">Sample Text</div><div class="chip" style="left:76px;top:82px">Sample Text</div><div class="chip" style="left:126px;top:82px">Sample Text</div>
  <div class="tx" style="left:20px;top:90px;width:38px;text-align:center">We focus on strategic business development to the top.</div>
  <div class="tx" style="left:70px;top:90px;width:38px;text-align:center">We focus on strategic business development to the top.</div>
  <div class="tx" style="left:120px;top:90px;width:38px;text-align:center">We focus on strategic business development to the top.</div>
  <div class="foot"><span>www.tolvik-advisory.se</span><span>Page • 4</span></div>
</div>
<div class="num" style="left:378px;top:760px">22</div>

<div class="slide" style="left:431px;top:624px">
  <div class="photo p-wb" style="left:0;top:0;width:172px;height:128px" role="img" aria-label="Consultant sketching ideas on a whiteboard"></div>
  <div class="ab red" style="left:74px;top:44px;width:98px;height:64px"></div>
  <div class="ab inv" style="left:80px;top:50px;font-size:7px">Sample Text</div>
  <div class="tx w" style="left:80px;top:62px;width:86px">We focus on strategic business development and work in close cooperation with the customer to make sure it is the customer that will become the hero, our work is to support and guide them to the top.</div>
</div>
<div class="num" style="left:588px;top:760px">23</div>

<div class="slide" style="left:641px;top:624px">
  <div class="ab red" style="left:0;top:0;width:28px;height:128px"></div>
  <div class="ttl" style="left:38px;top:12px">Sample Text</div><div class="logo">tolvik<i></i></div>
  <div class="photo p-man" style="left:16px;top:36px;width:48px;height:60px" role="img" aria-label="Portrait of a consultant"></div>
  <div class="tx" style="left:80px;top:32px;width:82px"><span style="color:var(--red)">Name</span><br>Designation<br>We focus on strategic business development and work in close cooperation with the customer.</div>
  <svg class="ab" style="left:84px;top:62px" width="72" height="44" viewBox="0 0 72 44">
    <line x1="2" y1="0" x2="2" y2="36" stroke="#999" stroke-width=".5"/>
    <g fill="#6f9a3c"><rect x="3" y="2" width="40" height="2"/><rect x="3" y="7" width="30" height="2"/><rect x="3" y="12" width="48" height="2"/><rect x="3" y="17" width="36" height="2"/><rect x="3" y="22" width="44" height="2"/><rect x="3" y="27" width="24" height="2"/><rect x="3" y="32" width="52" height="2"/></g>
  </svg>
  <div class="foot" style="left:30px"><span>www.tolvik-advisory.se</span><span>Page • 4</span></div>
</div>
<div class="num" style="left:798px;top:760px">24</div>

<div class="slide" style="left:850px;top:624px">
  <div class="ttl">Sample Text</div><div class="logo">tolvik<i></i></div>
  <svg class="ab" style="left:0;top:34px" width="172" height="48" viewBox="0 0 172 48">
    <polygon points="0,14 134,14 134,0 162,24 134,48 134,34 0,34" fill="#c6c8cc"/>
    <rect x="14" y="6" width="24" height="36" rx="3" fill="#c0223f"/>
    <rect x="44" y="6" width="24" height="36" rx="3" fill="#135b8e"/>
    <rect x="74" y="6" width="24" height="36" rx="3" fill="#c0223f"/>
    <rect x="104" y="6" width="24" height="36" rx="3" fill="#135b8e"/>
    <g fill="#fff" font-size="3" font-family="Didact Gothic,sans-serif"><text x="17" y="32">Sample Text</text><text x="47" y="32">Sample Text</text><text x="77" y="32">Sample Text</text><text x="107" y="32">Sample Text</text><text x="136" y="26">RESULT</text></g>
  </svg>
  <div class="tx" style="left:20px;top:90px;width:132px;text-align:center">We focus on strategic business development and work in close cooperation with the customer to make sure it is the customer that will become the hero, our work is to support and guide them to the top.</div>
  <div class="foot"><span>www.tolvik-advisory.se</span><span>Page • 4</span></div>
</div>
<div class="num" style="left:1008px;top:760px">25</div>

<div class="slide" style="left:1032px;top:628px;height:114px">
  <div class="ttl">Sample Text</div><div class="logo">tolvik<i></i></div>
  <div class="ab" style="left:0;top:38px;width:90px;height:2px;background:var(--red)"></div>
  <svg class="ab" style="left:48px;top:24px" width="46" height="46" viewBox="0 0 46 46">
    <path d="M23 3 A20 20 0 1 1 3 23" fill="none" stroke="#c0223f" stroke-width="5"/>
    <path d="M3 23 A20 20 0 0 1 23 3" fill="none" stroke="#135b8e" stroke-width="5"/>
    <circle cx="23" cy="23" r="8" fill="#c0223f"/>
  </svg>
  <div class="ab" style="left:16px;top:44px;font:700 7px Montserrat,sans-serif;color:var(--red)">$88b</div>
  <div class="ab" style="left:118px;top:70px;font:700 7px Montserrat,sans-serif;color:var(--blue)">$68b</div>
  <div class="tx" style="left:8px;top:54px;width:40px"><span style="color:var(--red)">Sample Text</span><br>We focus on strategic business for the hero.</div>
  <div class="tx" style="left:116px;top:34px;width:50px"><span style="color:var(--blue)">Sample Text</span><br>We focus on strategic business for the hero.</div>
  <div class="foot"><span>www.tolvik-advisory.se</span><span>Page • 4</span></div>
</div>

<!-- Row 6 -->
<div class="slide" style="left:12px;top:782px">
  <div class="ttl">Sample Text</div><div class="logo">tolvik<i></i></div>
  <svg class="ab" style="left:10px;top:44px" width="152" height="20" viewBox="0 0 152 20">
    <line x1="6" y1="10" x2="152" y2="10" stroke="#999" stroke-width=".6"/>
    <circle cx="10" cy="10" r="5" fill="#fff" stroke="#c0223f" stroke-width="1.6"/>
    <circle cx="38" cy="10" r="2" fill="#6f9a3c"/><circle cx="62" cy="10" r="2" fill="#135b8e"/><circle cx="82" cy="10" r="2" fill="#135b8e"/>
    <circle cx="100" cy="10" r="5" fill="#fff" stroke="#c0223f" stroke-width="1.6"/>
    <circle cx="126" cy="10" r="2" fill="#6f9a3c"/><circle cx="148" cy="10" r="2" fill="#135b8e"/>
  </svg>
  <div class="tx" style="left:24px;top:32px;transform:rotate(-60deg);color:var(--red)">Sample Text</div>
  <div class="tx" style="left:112px;top:32px;transform:rotate(-60deg);color:var(--red)">Sample Text</div>
  <div class="tx" style="left:44px;top:70px;transform:rotate(-60deg)">Sample Text</div>
  <div class="tx" style="left:70px;top:70px;transform:rotate(-60deg)">Sample Text</div>
  <div class="tx" style="left:140px;top:70px;transform:rotate(-60deg)">Sample Text</div>
  <div class="tx" style="left:20px;top:90px;width:132px;text-align:center">We focus on strategic business development and work in close cooperation with the customer to make sure it is the customer that will become the hero, our work is to support and guide them to the top.</div>
  <div class="foot"><span>www.tolvik-advisory.se</span><span>Page • 4</span></div>
</div>

<div class="slide" style="left:221px;top:782px">
  <div class="ttl">Sample Text</div><div class="logo">tolvik<i></i></div>
  <svg class="ab" style="left:0;top:36px" width="172" height="44" viewBox="0 0 172 44">
    <line x1="0" y1="18" x2="138" y2="18" stroke="#135b8e" stroke-width="2.5"/><polygon points="136,13 144,18 136,23" fill="#135b8e"/>
    <g stroke="#135b8e" stroke-width="1.5"><line x1="24" y1="6" x2="24" y2="16"/><line x1="64" y1="6" x2="64" y2="16"/><line x1="104" y1="6" x2="104" y2="16"/><line x1="44" y1="20" x2="44" y2="30"/><line x1="84" y1="20" x2="84" y2="30"/><line x1="124" y1="20" x2="124" y2="30"/></g>
    <g fill="#135b8e"><polygon points="21,14 27,14 24,18"/><polygon points="61,14 67,14 64,18"/><polygon points="101,14 107,14 104,18"/><polygon points="41,28 47,28 44,32"/><polygon points="81,28 87,28 84,32"/><polygon points="121,28 127,28 124,32"/></g>
  </svg>
  <div class="chip" style="left:14px;top:38px">Sample Text</div><div class="chip" style="left:54px;top:38px">Sample Text</div><div class="chip" style="left:94px;top:38px">Sample Text</div>
  <div class="chip" style="left:146px;top:50px">Sample Text</div>
  <div class="chip" style="left:34px;top:70px">Sample Text</div><div class="chip" style="left:74px;top:70px">Sample Text</div><div class="chip" style="left:114px;top:70px">Sample Text</div>
  <div class="tx" style="left:20px;top:86px;width:132px;text-align:center">We focus on strategic business development and work in close cooperation with the customer to make sure it is the customer that will become the hero, our work is to support and guide them to the top.</div>
  <div class="foot"><span>www.tolvik-advisory.se</span><span>Page • 4</span></div>
</div>

<div class="slide" style="left:431px;top:782px">
  <div class="ttl">Sample Text</div><div class="logo">tolvik<i></i></div>
  <div class="dot red" style="left:10px;top:44px;width:24px;height:24px"></div>
  <div class="dot olive" style="left:34px;top:28px;width:24px;height:24px"></div>
  <div class="dot blue" style="left:60px;top:40px;width:24px;height:24px"></div>
  <div class="dot red" style="left:90px;top:34px;width:38px;height:38px"></div>
  <div class="dot olive" style="left:130px;top:28px;width:26px;height:26px"></div>
  <div class="tx w" style="left:14px;top:58px">Sample Text</div><div class="tx w" style="left:38px;top:42px">Sample Text</div><div class="tx w" style="left:64px;top:54px">Sample Text</div><div class="tx w" style="left:100px;top:58px">Sample Text</div><div class="tx w" style="left:134px;top:42px">Sample Text</div>
  <div class="tx" style="left:20px;top:86px;width:132px;text-align:center">We focus on strategic business development and work in close cooperation with the customer to make sure it is the customer that will become the hero, our work is to support and guide them to the top.</div>
  <div class="foot"><span>www.tolvik-advisory.se</span><span>Page • 4</span></div>
</div>

<div class="slide" style="left:641px;top:782px">
  <div class="ttl">Sample Text</div><div class="logo">tolvik<i></i></div>
  <div class="dot red" style="left:14px;top:30px;width:9px;height:9px"></div>
  <div class="tx" style="left:30px;top:30px;width:132px">We focus on strategic business development and work in close cooperation with the customer to make sure it is the customer that will become the hero, our work is to support and guide them.</div>
  <div class="dot olive" style="left:14px;top:56px;width:9px;height:9px"></div>
  <div class="tx" style="left:30px;top:56px;width:132px">We focus on strategic business development and work in close cooperation with the customer to make sure it is the customer that will become the hero, our work is to support and guide them.</div>
  <div class="dot blue" style="left:14px;top:82px;width:9px;height:9px"></div>
  <div class="tx" style="left:30px;top:82px;width:132px">We focus on strategic business development and work in close cooperation with the customer to make sure it is the customer that will become the hero, our work is to support and guide them.</div>
  <div class="foot"><span>www.tolvik-advisory.se</span><span>Page • 4</span></div>
</div>

<div class="slide" style="left:850px;top:782px">
  <div class="ttl">Sample Text</div><div class="logo">tolvik<i></i></div>
  <div class="photo p-team" style="left:20px;top:22px;width:46px;height:30px" role="img" aria-label="Business team meeting"></div>
  <div class="photo p-wb" style="left:104px;top:22px;width:46px;height:30px" role="img" aria-label="Consultant at a whiteboard"></div>
  <div class="chip" style="left:26px;top:56px">Sample Text</div><div class="chip" style="left:110px;top:56px">Sample Text</div>
  <div class="tx" style="left:16px;top:64px;width:58px">We focus on strategic business development and work in close cooperation with the customer to make sure it is the customer that will become the hero.</div>
  <div class="tx" style="left:100px;top:64px;width:58px">We focus on strategic business development and work in close cooperation with the customer to make sure it is the customer that will become the hero.</div>
  <div class="foot"><span>www.tolvik-advisory.se</span><span>Page • 4</span></div>
</div>

<div class="slide" style="left:1034px;top:780px">
  <div class="ttl">Sample Text</div>
  <div class="photo p-city" style="left:100px;top:0;width:72px;height:118px" role="img" aria-label="Hand raised among city skyscrapers"></div>
  <div class="dot red" style="left:10px;top:26px;width:7px;height:7px"></div><div class="tx" style="left:22px;top:26px;width:76px">We focus on strategic business development, our work is to support and guide them to the top.</div>
  <div class="dot blue" style="left:10px;top:46px;width:7px;height:7px"></div><div class="tx" style="left:22px;top:46px;width:76px">We focus on strategic business development, our work is to support and guide them to the top.</div>
  <div class="dot red" style="left:10px;top:66px;width:7px;height:7px"></div><div class="tx" style="left:22px;top:66px;width:76px">We focus on strategic business development, our work is to support and guide them to the top.</div>
  <div class="ab red" style="left:6px;top:96px;width:108px;height:16px"></div>
  <div class="tx w" style="left:10px;top:98px;width:100px">We focus on strategic business development and work in close cooperation with the customer to guide them.</div>
  <div class="foot"><span>www.tolvik-advisory.se</span><span>Page • 4</span></div>
</div>

<!-- Row 7 -->
<div class="slide" style="left:24px;top:924px">
  <div class="photo" style="left:0;top:0;width:172px;height:128px;background:linear-gradient(160deg,#c0223f,#a01c34 60%,#c33a4c)" role="img" aria-label="Red-toned mountain landscape"></div>
  <div class="dot" style="left:156px;top:6px;width:8px;height:6px;background:#fff"></div>
  <div class="dot" style="left:28px;top:48px;width:14px;height:14px;border:1.5px solid #fff"></div>
  <div class="ab inv" style="left:22px;top:72px;font-size:7px">Section Title</div>
  <div class="tx w" style="left:22px;top:86px;width:100px;font-size:3.4px;line-height:1.5">We Focus On Strategic Business Become The Hero, Our Work Is To Support And Guide Them To The Top.</div>
</div>
<div class="num" style="left:182px;top:1060px">46</div>

<div class="slide" style="left:234px;top:924px">
  <svg class="ab" style="left:0;top:0" width="172" height="128" viewBox="0 0 172 128"><polygon points="0,0 160,0 0,128" fill="#c0223f"/></svg>
  <div class="ab inv" style="left:10px;top:20px;font-size:11px">tolvik</div>
  <div class="dot" style="left:72px;top:50px;width:14px;height:14px;background:#fff;border:1px solid #bbb"></div>
  <div class="ab" style="left:74px;top:70px;font-size:7px;color:var(--red)">Section Title</div>
  <div class="tx" style="left:74px;top:84px;width:90px;font-size:3.4px;line-height:1.5">We Focus On Strategic Business Become The Hero, Our Work Is To Support And Guide Them To The Top.</div>
</div>
<div class="num" style="left:390px;top:1060px">47</div>

<div class="slide" style="left:444px;top:924px">
  <div class="photo" style="left:0;top:0;width:172px;height:128px;background:linear-gradient(160deg,#c0223f,#a01c34 60%,#c33a4c)" role="img" aria-label="Red-toned mountain landscape"></div>
  <div class="dot" style="left:82px;top:34px;width:8px;height:6px;background:#fff"></div>
  <div class="big inv" style="top:52px;font:700 9px Montserrat,sans-serif">Thank You For Your Time</div>
  <div class="tx w" style="left:0;width:172px;top:70px;text-align:center;font-size:3.4px;line-height:1.6">48 Harbor Lane,<br>Eastvale, 10233<br><br>Call Us<br><br>Mail Us</div>
</div>
<div class="num" style="left:600px;top:1060px">48</div>

<div class="slide" style="left:654px;top:924px">
  <div class="photo" style="left:0;top:0;width:172px;height:56px;background:linear-gradient(160deg,#c0223f,#a01c34 60%,#c33a4c)" role="img" aria-label="Red-toned mountain landscape"></div>
  <div class="big" style="top:24px;font-size:9px;color:#f4d3da">Thank You For Your Time</div>
  <div class="ab red" style="left:70px;top:52px;width:32px;height:8px"></div>
  <div class="ab inv" style="left:78px;top:53px;font-size:4px">tolvik</div>
  <div class="tx" style="left:60px;top:68px;font-size:3.4px;line-height:2.4">⌖ 48 Harbor Lane, Eastvale, 10233<br>☏ Call Us<br>✉ Mail Us</div>
</div>
<div class="num" style="left:810px;top:1060px">49</div>

<div class="slide" style="left:838px;top:928px;width:172px;height:124px">
  <div class="photo p-lake" style="left:0;top:0;width:82px;height:124px" role="img" aria-label="Cliffs above a lake"></div>
  <div class="ttl" style="left:94px;top:16px">Sample Text</div>
  <div class="tx" style="left:94px;top:32px;width:70px">• Get help from the world's largest friendly freelance market across every skill.<br><br>• The marketplace platform seamlessly hosts all your work and payments.<br><br>• The platform helps you find trusted talent quickly and deliver great work.</div>
  <div class="foot"><span>www.tolvik-advisory.se</span><span>Page • 4</span></div>
</div>

<div class="slide" style="left:1024px;top:928px;height:128px;border:1.5px solid #e8c860">
  <div class="ttl">Sample Text</div><div class="logo">tolvik<i></i></div>
  <div class="photo p-team" style="left:10px;top:28px;width:52px;height:50px" role="img" aria-label="Business team meeting"></div>
  <div class="dot red" style="left:74px;top:26px;width:8px;height:8px"></div><div class="tx" style="left:88px;top:26px;width:76px">We focus on strategic business development and work in close cooperation, our work is to guide them.</div>
  <div class="dot blue" style="left:74px;top:54px;width:8px;height:8px"></div><div class="tx" style="left:88px;top:54px;width:76px">We focus on strategic business development and work in close cooperation, our work is to guide them.</div>
  <div class="dot red" style="left:74px;top:82px;width:8px;height:8px"></div><div class="tx" style="left:88px;top:82px;width:76px">We focus on strategic business development and work in close cooperation, our work is to guide them.</div>
  <div class="foot"><span>www.tolvik-advisory.se</span><span>Page • 4</span></div>
</div>
</body>
</html>
```